Broschüren-Design für Versicherungsagenten
Zielgruppe
Ich bin mit KL-Vorsorge als unabhängiger Versicherungsagent Selbstständig. (www.kl-vorsorge.de)
Ich habe mich auf die Absicherung von biometrischen Risiken spezialisiert - die auch in der Broschüre Thematisiert werden sollen. Das Oberthema der Broschüre ist 'biometrische Risiken'. Dies soll dann auf die Themen: Arbeitskraft, Langlebigkeit und Pflege heruntergebrochen werden.
Zielgruppe sind vor allem junge Menschen, die gerade erst eine Ausbildung gestartet oder ihr Studium beendet haben.
Aufgabenstellung
Das Design sollte die drei Hauptbereiche: Arbeitskraft, Langlebigkeit und Pflege, leicht verständlich dem Kunden veranschaulichen. Texte, Informationen und Grafiken (in der Reihenfolge, so wie ich mir das vorstelle) sind als Datei beigefügt.
Das ganze soll im DIN A4 Format gedruckt werden, wobei ich auf einen Hochwertigen Druck inklusive Druckveredelung hohen Wert lege.

```html
<!DOCTYPE html>
<html lang="de">
<head>
<meta charset="utf-8">
<title>KL-Vorsorge – Broschüre Biometrische Risiken</title>
<link rel="stylesheet" href="https://fonts.googleapis.com/css2?family=Montserrat:wght@400;500;700&family=Share+Tech+Mono&display=swap">
<style>
  :root {
    --stage: #e4e4e4;
    --paper: #d9d9d9;
    --paper-light: #e6e6e6;
    --band: #d3a162;
    --band-dark: #c99451;
    --ink: #1c1c1c;
    --ink-soft: #3a3a3a;
    --photo-light: #b8b6b2;
    --photo-dark: #5e5c59;
  }
  * { margin: 0; padding: 0; box-sizing: border-box; }
  html, body { width: 1200px; height: 857px; overflow: hidden; }
  body {
    background: var(--stage);
    font-family: "Montserrat", Arial, sans-serif;
    color: var(--ink);
    position: relative;
  }
  .spread {
    position: absolute;
    left: 40px;
    top: 230px;
    width: 1120px;
    height: 396px;
    display: flex;
    box-shadow: 0 14px 30px rgba(0,0,0,0.18);
  }
  .page {
    position: relative;
    width: 560px;
    height: 396px;
    overflow: hidden;
  }
  .page--back {
    background: linear-gradient(90deg, var(--paper-light) 0%, var(--paper) 85%, #cdcdcd 100%);
  }
  .page--front {
    background: linear-gradient(90deg, #cfcfcf 0%, var(--paper-light) 12%, var(--paper-light) 100%);
  }
  .band {
    position: absolute;
    left: 0;
    width: 100%;
    background: linear-gradient(90deg, var(--band-dark), var(--band));
    display: flex;
    align-items: center;
    font-family: "Share Tech Mono", "Courier New", monospace;
    font-size: 22px;
    letter-spacing: 6px;
    color: var(--ink);
    text-transform: uppercase;
  }
  .page--back .band { top: 150px; height: 52px; padding-left: 50px; }
  .page--front .band { top: 70px; height: 44px; padding-left: 30px; font-size: 20px; }
  .band__arrows { margin-left: 28px; letter-spacing: 2px; }
  .brand {
    display: flex;
    align-items: center;
    gap: 8px;
  }
  .brand__dot {
    border-radius: 50%;
    background: var(--ink);
    flex: none;
  }
  .brand__name { font-weight: 700; color: var(--ink); }
  .contact {
    position: absolute;
    left: 50px;
    top: 238px;
  }
  .contact .brand__dot { width: 30px; height: 30px; }
  .contact .brand__name { font-size: 24px; }
  .contact__owner { font-size: 10px; font-weight: 700; margin: 6px 0 0 38px; }
  .contact__lines {
    margin-top: 4px;
    font-size: 10.5px;
    line-height: 1.35;
    color: var(--ink-soft);
    list-style: none;
  }
  .contact__lines strong { color: var(--ink); }
  .front-brand {
    position: absolute;
    left: 26px;
    top: 26px;
  }
  .front-brand .brand__dot { width: 16px; height: 16px; }
  .front-brand .brand__name { font-size: 12px; font-weight: 500; }
  .cover-photo {
    position: absolute;
    left: 0;
    top: 114px;
    width: 100%;
    height: 282px;
    background: linear-gradient(160deg, var(--photo-light) 0%, #8f8d89 55%, var(--photo-dark) 100%);
  }
</style>
</head>
<body>
  <main class="spread">
    <section class="page page--back" aria-label="Rückseite">
      <div class="band"><span>Kontakt</span><span class="band__arrows">&gt;&gt;&gt;</span></div>
      <div class="contact">
        <div class="brand">
          <span class="brand__dot"></span>
          <span class="brand__name">KL-Vorsorge</span>
        </div>
        <ul class="contact__lines">
          <li><strong>KL-Vorsorge – Max Belwig</strong></li>
          <li>Birkenallee 12,</li>
          <li>70173 Stuttgart</li>
          <li>Tel.: 0151 48203917</li>
          <li>E-Mail: max.belwig@mailpost.de</li>
        </ul>
      </div>
    </section>
    <section class="page page--front" aria-label="Titelseite">
      <div class="front-brand brand">
        <span class="brand__dot"></span>
        <span class="brand__name">KL-Vorsorge</span>
      </div>
      <div class="band"><span>Biometrische Risiken</span><span class="band__arrows">&gt;&gt;&gt;</span></div>
      <div class="cover-photo" role="img" aria-label="Schwarz-Weiß-Foto einer Gruppe junger Menschen, die gemeinsam durch eine Halle gehen"></div>
    </section>
  </main>
</body>
</html>
```